Sumvane financial services stationery design

We need business stationery designed with letterheads, business cards, with compliments and envelope for a business that offers tax and accounting services

Designs look the same

Target Market(s)

Small to medium businesses, individuals, Self managed superfunds

Industry/Entity Type

Business

Font styles to use
Serif
Other font styles liked:
• Atlanta

Colors
32a6d6
3277b5

Requirements
Must have
• Logo incorporated with all my stationery
• professional
Should not have
• Lots of colours
• Busy

```html
<!DOCTYPE html>
<html lang="en">
<head>
<meta charset="utf-8">
<title>Sumvane Financial Services – Stationery</title>
<link href="https://fonts.googleapis.com/css2?family=Cinzel:wght@400;600&family=Roboto:wght@400;500&family=Great+Vibes&display=swap" rel="stylesheet">
<style>
:root{
  --blue:#2b77b1;
  --sky:#32a6d6;
  --paper:#f4f4f4;
  --stage:#ebebeb;
  --ink:#444;
  --faint:#e1e7ec;
  --faint-on-blue:#3a84bd;
}
*{margin:0;padding:0;box-sizing:border-box}
html,body{width:1200px;height:822px;overflow:hidden;background:var(--stage)}
body{position:relative;font-family:"Roboto",sans-serif;color:var(--ink)}
.sheet{position:absolute;background:var(--paper);overflow:hidden;box-shadow:0 1px 4px rgba(0,0,0,.12)}

/* brand lockup */
.brand{position:absolute;display:flex;align-items:center;gap:5px;font-family:"Cinzel",serif;font-weight:600;color:var(--ink)}
.brand .square{background:var(--blue);flex:none}
.brand .words{display:flex;flex-direction:column;line-height:1}
.brand .sub{font-weight:400;letter-spacing:.12em;margin-top:2px}
.brand.on-blue{color:#fff}
.brand.on-blue .square{background:#fff}

.faint-square{position:absolute;background:var(--faint);border-radius:8%}
.small{font-size:5px;line-height:1.45}
.band{position:absolute;background:var(--blue)}
.band .tail{position:absolute;right:0;top:0;bottom:0;background:var(--sky)}

/* letterhead */
.letterhead{left:349px;top:111px;width:313px;height:445px}
.letterhead .band{left:0;top:37px;width:216px;height:24px;display:flex;align-items:center;color:#fff;padding-left:17px;gap:10px}
.letterhead .band .divider{width:1px;height:14px;background:#fff}
.letterhead .brand{left:187px;top:37px;font-size:15px}
.letterhead .brand .square{width:26px;height:26px}
.letterhead .brand .sub{font-size:4px}
.letterhead .faint-square{left:70px;top:161px;width:173px;height:175px}
.letterhead .web{position:absolute;left:0;right:0;top:422px;text-align:center;font-size:6px;letter-spacing:.45em}

/* folder */
.folder{left:705px;top:91px;width:370px;height:467px;background:var(--blue)}
.folder .spine{position:absolute;top:0;bottom:0;width:1px;background:#2069a0}
.folder .brand{left:84px;top:208px;font-size:34px;gap:12px}
.folder .brand .square{width:54px;height:54px}
.folder .brand .sub{font-size:9px;letter-spacing:.16em}

/* business cards */
.card-back{left:168px;top:373px;width:141px;height:81px;background:var(--blue)}
.card-back .faint-square{left:66px;top:2px;width:76px;height:76px;background:var(--faint-on-blue)}
.card-back .brand{left:7px;top:50px;font-size:13px}
.card-back .brand .sub{font-size:3.4px}
.card-back .url{position:absolute;left:9px;top:70px;font-size:3.6px;color:#fff;letter-spacing:.2em}

.card-front{left:168px;top:476px;width:143px;height:81px}
.card-front .band{left:0;top:11px;width:82px;height:15px;color:#fff;padding:2px 0 0 9px}
.card-front .band .name{font-size:5px;font-weight:500}
.card-front .band .role{font-size:3.2px}
.card-front .brand{left:74px;top:11px;font-size:10px;gap:3px}
.card-front .brand .square{width:16px;height:16px}
.card-front .brand .sub{font-size:2.8px}
.card-front .contact{position:absolute;left:9px;top:55px;font-size:3.4px}
.card-front .address{position:absolute;right:9px;top:61px;font-size:3.4px;text-align:right}

/* envelopes and compliment slip */
.envelope-back{left:47px;top:602px;width:351px;height:167px}
.envelope-back .brand{left:22px;top:20px;font-size:13px}
.envelope-back .brand .square{width:22px;height:22px}
.envelope-back .brand .sub{font-size:3.5px}
.envelope-back .address{position:absolute;left:22px;top:50px;font-size:5px}
.envelope-back .faint-square{left:203px;top:19px;width:130px;height:150px}

.bottom-band{left:0;right:0;top:150px;height:10px}
.bottom-band .tail{width:40px}
.bottom-band .mark{position:absolute;right:40px;top:1px;width:10px;height:8px;background:#fff}

.envelope-front{left:433px;top:602px;width:351px;height:167px}
.envelope-front .flap{position:absolute;left:0;top:0;width:351px;height:60px;background:var(--blue);clip-path:polygon(0 0,100% 0,100% 55%,98% 100%,2% 100%,0 55%)}
.envelope-front .brand{left:145px;top:20px;font-size:11px;gap:3px}
.envelope-front .brand .square{width:16px;height:16px}
.envelope-front .brand .sub{font-size:3px}

.compliments{left:814px;top:602px;width:351px;height:167px}
.compliments .brand{left:22px;top:22px;font-size:13px}
.compliments .brand .square{width:22px;height:22px}
.compliments .brand .sub{font-size:3.5px}
.compliments .address{position:absolute;left:196px;top:22px;text-align:right;font-size:4.4px}
.compliments .divider{position:absolute;left:267px;top:22px;width:1px;height:22px;background:#999}
.compliments .contact{position:absolute;left:272px;top:21px;font-size:4.4px}
.compliments .greeting{position:absolute;left:0;right:0;top:84px;text-align:center;font-family:"Great Vibes",cursive;font-size:29px;color:var(--blue)}
</style>
</head>
<body>

<section class="sheet letterhead" aria-label="Letterhead">
  <div class="band small">
    <div>214 Harbour Row<br>Milford, Oregon 40218</div>
    <div class="divider"></div>
    <div>&#9742; 555 310 2748<br>&#9633; daniel@sumvane.com</div>
  </div>
  <div class="brand"><span class="square"></span><span class="words">Sumvane<span class="sub">Financial Services</span></span></div>
  <div class="faint-square"></div>
  <div class="web">www.sumvane.com</div>
</section>

<section class="sheet folder" aria-label="Presentation folder">
  <div class="spine" style="left:10px"></div>
  <div class="spine" style="left:15px"></div>
  <div class="spine" style="left:21px"></div>
  <div class="brand on-blue"><span class="square"></span><span class="words">Sumvane<span class="sub">Financial Services</span></span></div>
</section>

<section class="sheet card-back" aria-label="Business card, back">
  <div class="faint-square"></div>
  <div class="brand on-blue"><span class="words">Sumvane<span class="sub">Financial Services</span></span></div>
  <div class="url">www.sumvane.com</div>
</section>

<section class="sheet card-front" aria-label="Business card, front">
  <div class="band"><div class="name">DANIEL HART</div><div class="role">MANAGING DIRECTOR</div></div>
  <div class="brand"><span class="square"></span><span class="words">Sumvane<span class="sub">Financial Services</span></span></div>
  <div class="contact">555 310 2748<br>555 310 2749<br>555 310 2750<br>daniel@sumvane.com</div>
  <div class="address">214 Harbour Row<br>Milford, Oregon 40218<br>www.sumvane.com</div>
</section>

<section class="sheet envelope-back" aria-label="Envelope, back">
  <div class="brand"><span class="square"></span><span class="words">Sumvane<span class="sub">Financial Services</span></span></div>
  <div class="address">214 Harbour Row<br>Milford, Oregon 40218</div>
  <div class="faint-square"></div>
  <div class="band bottom-band"><span class="mark"></span><span class="tail"></span></div>
</section>

<section class="sheet envelope-front" aria-label="Envelope, front">
  <div class="flap"></div>
  <div class="brand on-blue"><span class="square"></span><span class="words">Sumvane<span class="sub">Financial Services</span></span></div>
</section>

<section class="sheet compliments" aria-label="With compliments slip">
  <div class="brand"><span class="square"></span><span class="words">Sumvane<span class="sub">Financial Services</span></span></div>
  <div class="address">214 Harbour Row<br>Milford, Oregon 40218<br>www.sumvane.com</div>
  <div class="divider"></div>
  <div class="contact">555 310 2748<br>555 310 2749<br>555 310 2750<br>daniel@sumvane.com</div>
  <div class="greeting">With Compliments</div>
  <div class="band bottom-band"><span class="mark"></span><span class="tail"></span></div>
</section>

</body>
</html>
```